10-year customer thank you card

We want a greeting card that our sales reps can send to companies/customers who have been with our company for 10 or more years. We're a software company, our corporate color is blue but we also like green, orange, and purple. We'd like something rather minimal/simplistic for this card, perhaps building off our tree logo. We're really open to ideas for this one. You must use the template files that are uploaded. Copy included in 10 year thank you card file; the copy may change based on how it looks when laid out
Updates

I updated our brief. We'd prefer a sans serif font. I also uploaded a blank infographic image that includes more of our approved colors.

Industry/Entity Type

Software

Font styles to use
Sans Serif

```html
<!DOCTYPE html>
<html lang="en">
<head>
<meta charset="utf-8">
<title>Bayridge Software – 10 Years Thank You Card</title>
<link rel="stylesheet" href="https://fonts.googleapis.com/css2?family=Montserrat:wght@700;800&family=Tinos&display=swap">
<style>
  :root {
    --paper: #ffffff;
    --leaf-green: #8dc648;
    --sun-orange: #f47b3a;
    --edge-peach: #f3b07a;
    --brand-blue: #1e80c8;
    --ink: #1a1a1a;
  }
  html, body {
    margin: 0;
    padding: 0;
    overflow: hidden;
    background: var(--paper);
  }
  .card {
    position: relative;
    width: 869px;
    height: 1200px;
    background: var(--paper);
    overflow: hidden;
  }
  .anniversary-mark {
    position: absolute;
    left: 0;
    top: 0;
    width: 869px;
    height: 600px;
  }
  .numeral { fill: var(--leaf-green); }
  .numeral-edge { fill: var(--edge-peach); }
  .years-word {
    fill: var(--sun-orange);
    font-family: "Montserrat", sans-serif;
    font-weight: 800;
    font-size: 56px;
    letter-spacing: 6px;
  }
  .center-name {
    fill: var(--brand-blue);
    font-family: "Montserrat", sans-serif;
    font-weight: 700;
    font-size: 44px;
  }
  .signoff {
    position: absolute;
    left: 0;
    width: 100%;
    top: 886px;
    text-align: center;
    font-family: "Tinos", serif;
    color: var(--ink);
  }
  .company-line {
    display: inline-flex;
    align-items: center;
    gap: 12px;
    font-size: 38px;
    line-height: 1;
  }
  .company-dot {
    width: 26px;
    height: 26px;
    border-radius: 50%;
    background: var(--brand-blue);
  }
  .company-url {
    margin-top: 20px;
    font-size: 26px;
    letter-spacing: 1px;
  }
</style>
</head>
<body>
<main class="card">
  <svg class="anniversary-mark" viewBox="0 0 869 600" aria-label="10 years, set upside down">
    <defs>
      <clipPath id="numeral-crop">
        <rect x="0" y="145" width="869" height="455"/>
      </clipPath>
    </defs>
    <g clip-path="url(#numeral-crop)">
      <!-- soft peach edge beneath the green numerals -->
      <g class="numeral-edge" transform="translate(3,4)">
        <path fill-rule="evenodd" d="M75 282a255 255 0 1 0 510 0a255 255 0 1 0 -510 0Z M158 282a175 175 0 1 0 350 0a175 175 0 1 0 -350 0Z"/>
        <rect x="612" y="140" width="88" height="395"/>
        <polygon points="700,430 775,418 775,490 730,510 700,535"/>
      </g>
      <g class="numeral">
        <path fill-rule="evenodd" d="M75 282a255 255 0 1 0 510 0a255 255 0 1 0 -510 0Z M158 282a175 175 0 1 0 350 0a175 175 0 1 0 -350 0Z"/>
        <rect x="612" y="140" width="88" height="395"/>
        <polygon points="700,430 775,418 775,490 730,510 700,535"/>
      </g>
    </g>
    <text class="center-name" x="330" y="262" text-anchor="middle" transform="rotate(180 330 262)">Bayridge</text>
    <text class="years-word" x="325" y="100" text-anchor="middle" transform="rotate(180 325 100)" dominant-baseline="middle">YEARS</text>
  </svg>

  <footer class="signoff">
    <div class="company-line"><span class="company-dot"></span>Bayridge Software</div>
    <div class="company-url">www.bayridgesoft.com</div>
  </footer>
</main>
</body>
</html>
```